Kestrel Flooring Supply

Basic one-sided business card design using the attached logo. Vintage americana theme. Font is modified Arial Nova Cond, but anything that coordinates can be used

```html
<!DOCTYPE html>
<html lang="en">
<head>
<meta charset="utf-8">
<title>Kestrel Flooring Supply – Business Card</title>
<link rel="stylesheet" href="https://fonts.googleapis.com/css2?family=Roboto+Condensed:wght@400;700&display=swap">
<style>
  :root {
    --backdrop: #3c3c3c;
    --card-black: #050505;
    --card-back: #1c1c1c;
    --gold: #b8976a;
    --white: #f4f4f4;
    --grey: #bdbdbd;
    --divider: #5a5a5a;
  }
  * { box-sizing: border-box; margin: 0; padding: 0; }
  html, body {
    width: 1200px; height: 803px; overflow: hidden;
    background: var(--backdrop);
    font-family: "Roboto Condensed", Arial, sans-serif;
  }
  .stage {
    position: relative; width: 1200px; height: 803px;
    display: flex; align-items: center; justify-content: center; gap: 40px;
  }
  .card {
    position: relative; width: 540px; height: 309px;
    border-radius: 18px; overflow: hidden;
  }
  .card--front {
    background: var(--card-black);
    border-bottom: 5px solid var(--gold);
  }
  .brand-mark {
    position: absolute; left: 30px; top: 0; bottom: 0; width: 220px;
    display: flex; align-items: center; gap: 10px;
  }
  .brand-mark__dot {
    flex: none; width: 14px; height: 14px; border-radius: 50%;
    background: var(--gold);
  }
  .brand-mark__name {
    color: var(--white); font-weight: 700; font-size: 24px;
    line-height: 1.05; text-transform: uppercase; letter-spacing: 0.5px;
  }
  .divider {
    position: absolute; left: 262px; top: 36px; width: 1px; height: 237px;
    background: var(--divider);
  }
  .contact {
    position: absolute; left: 286px; top: 46px; right: 20px;
    color: var(--white); font-size: 14px; line-height: 1.35;
  }
  .contact__name { color: var(--gold); font-size: 24px; line-height: 1.1; }
  .contact__title { color: var(--grey); font-size: 13px; margin-bottom: 16px; }
  .contact__address { margin-bottom: 14px; }
  .contact__list { list-style: none; }
  .contact__list li { display: flex; align-items: center; gap: 8px; }
  .contact__icon { width: 12px; height: 12px; flex: none; fill: var(--gold); }
  .card--back {
    background: var(--card-back);
    border: 2px solid #d8d8d8;
  }
  .card__pattern {
    position: absolute; inset: 0;
    background: radial-gradient(circle at 50% 50%, #262626, #161616);
  }
  .back-mark {
    position: absolute; right: 24px; bottom: 100px;
    display: flex; align-items: center; gap: 6px;
  }
  .back-mark__dot { width: 8px; height: 8px; border-radius: 50%; background: var(--gold); }
  .back-mark__name { color: var(--white); font-weight: 700; font-size: 10px; text-transform: uppercase; }
</style>
</head>
<body>
<main class="stage">
  <section class="card card--front">
    <div class="brand-mark">
      <span class="brand-mark__dot"></span>
      <span class="brand-mark__name">Kestrel Flooring Supply</span>
    </div>
    <div class="divider"></div>
    <div class="contact">
      <p class="contact__name">Daniel Harrow</p>
      <p class="contact__title">President</p>
      <p class="contact__address">4412 Alder Crest Road<br>Fairbanks, Canada 29831</p>
      <ul class="contact__list">
        <li><svg class="contact__icon" viewBox="0 0 12 12"><path d="M2.5 0.5l2 2.5-1 1.2c0.7 1.5 1.8 2.6 3.3 3.3l1.2-1 2.5 2-1 2C5 10.5 1.5 7 0.5 1.5z"/></svg>555-218-4076</li>
        <li><svg class="contact__icon" viewBox="0 0 12 12"><rect x="3" y="0.5" width="6" height="11" rx="1" fill="none" stroke="#b8976a" stroke-width="1.2"/></svg>555-309-6621</li>
        <li><svg class="contact__icon" viewBox="0 0 12 12"><rect x="0.5" y="2" width="11" height="8" fill="#b8976a"/><path d="M0.5 2l5.5 4.5 5.5-4.5" fill="none" stroke="#050505" stroke-width="1"/></svg>info@kestrelflooringsupply.com</li>
        <li><svg class="contact__icon" viewBox="0 0 12 12"><circle cx="6" cy="6" r="5.5"/></svg>www.kestrelflooringsupply.com</li>
      </ul>
    </div>
  </section>
  <section class="card card--back">
    <div class="card__pattern" role="img" aria-label="Faint repeating brand pattern on dark background"></div>
    <div class="back-mark">
      <span class="back-mark__dot"></span>
      <span class="back-mark__name">Kestrel Flooring Supply</span>
    </div>
  </section>
</main>
</body>
</html>
```